Bright Fern Custom Homes business card. Double sided. Modern. professional

Bright Fern Custom Homes
contemporary modern design with our logo /
Double sided with all our contact information
Use same Green colors as in our Logo. Contemporary logo that grabs your attention. Visually pleasing and balanced. Easy to read, and Vibrant. Would love an option for rounded edges. Embossed logo would be amazing.
Contact Information for Business Card
Dana Welk Owner / General Contractor Bright Fern Custom Homes p: 704.552.1830 m: 912.648.2071 e: brightferncustomhomes@mailbox.example w: www.brightferncustomhomes.example 218 Pryor Meadow Lane Fernwood Falls, NC 28041

```html
<!DOCTYPE html>
<html lang="en">
<head>
<meta charset="utf-8">
<title>Bright Fern Custom Homes – Business Card</title>
<link href="https://fonts.googleapis.com/css2?family=Roboto:wght@400;700&display=swap" rel="stylesheet">
<style>
  :root {
    --page-bg: #e6e6e6;
    --card-white: #ffffff;
    --fern: #5c7332;
    --fern-back: #5d7033;
    --fern-deep: #52652c;
    --ink: #222222;
  }
  * { margin: 0; padding: 0; box-sizing: border-box; }
  html, body {
    width: 1200px; height: 1200px; overflow: hidden;
    background: var(--page-bg);
    font-family: "Roboto", Arial, sans-serif;
  }
  .card {
    position: absolute;
    left: 229px;
    width: 745px;
    height: 418px;
  }
  .card-front { top: 164px; background: var(--card-white); }
  .card-back { top: 620px; background: var(--fern-back); }

  .brand-lockup {
    position: absolute;
    left: 420px; top: 60px; width: 290px;
    text-align: center;
  }
  .brand-mark {
    width: 110px; height: 110px; border-radius: 50%;
    background: var(--fern);
    margin: 0 auto 22px;
  }
  .brand-name {
    font-weight: 400; font-size: 25px; line-height: 1.15;
    letter-spacing: 2px; color: var(--fern);
    text-transform: uppercase;
  }

  .holder-name {
    position: absolute; left: 25px; top: 188px;
    font-weight: 700; font-size: 32px; color: var(--fern);
  }
  .holder-role {
    position: absolute; left: 25px; top: 230px;
    font-size: 18px; color: var(--ink);
  }

  .contact-list {
    position: absolute; left: 25px; top: 286px;
    list-style: none;
  }
  .contact-list li {
    display: flex; align-items: center;
    height: 28px; font-size: 18px; color: var(--ink);
  }
  .contact-icon { width: 16px; height: 16px; margin-right: 4px; fill: var(--fern); flex: none; }

  .address {
    position: absolute; right: 27px; top: 338px;
    text-align: right; font-size: 18px; line-height: 28px; color: var(--ink);
    font-style: normal;
  }

  .back-name {
    position: absolute; inset: 0;
    display: flex; align-items: center; justify-content: center;
    font-weight: 400; font-size: 40px; letter-spacing: 3px;
    text-transform: uppercase; color: var(--fern-deep);
  }
</style>
</head>
<body>

<section class="card card-front" aria-label="Card front">
  <div class="brand-lockup">
    <div class="brand-mark"></div>
    <div class="brand-name">Bright Fern<br>Custom Homes</div>
  </div>

  <h1 class="holder-name">Dana Welk</h1>
  <p class="holder-role">Owner</p>

  <ul class="contact-list">
    <li>
      <svg class="contact-icon" viewBox="0 0 24 24" aria-hidden="true"><path d="M6.6 10.8a15 15 0 0 0 6.6 6.6l2.2-2.2a1 1 0 0 1 1-.25 11.4 11.4 0 0 0 3.6.57 1 1 0 0 1 1 1V20a1 1 0 0 1-1 1A17 17 0 0 1 3 4a1 1 0 0 1 1-1h3.5a1 1 0 0 1 1 1c0 1.25.2 2.45.57 3.57a1 1 0 0 1-.25 1z"/></svg>
      704.552.1830
    </li>
    <li>
      <svg class="contact-icon" viewBox="0 0 24 24" aria-hidden="true"><path d="M7 1h10a2 2 0 0 1 2 2v18a2 2 0 0 1-2 2H7a2 2 0 0 1-2-2V3a2 2 0 0 1 2-2zm0 3v15h10V4zm5 16.2a1 1 0 1 0 0 .01z"/></svg>
      912.648.2071
    </li>
    <li>
      <svg class="contact-icon" viewBox="0 0 24 24" aria-hidden="true"><path d="M2 6h20v1.2l-10 6-10-6zm0 3.4 10 6 10-6V19H2z"/></svg>
      brightferncustomhomes@mailbox.example
    </li>
    <li>
      <svg class="contact-icon" viewBox="0 0 24 24" aria-hidden="true"><circle cx="12" cy="12" r="10"/></svg>
      www.brightferncustomhomes.example
    </li>
  </ul>

  <address class="address">
    218 Pryor Meadow Lane<br>
    Fernwood Falls, NC 28041
  </address>
</section>

<section class="card card-back" aria-label="Card back">
  <div class="back-name">Bright Fern</div>
</section>

</body>
</html>
```